Stationery Design Project

We need a stationery design for a consultancy called 'Marlow Ridge'. The design should communicate innovation and professionalism. The colors used should complement our logo. Please include source files for winning design.

Requirements
Must have
• Logo with company name should be included. Font of the text in logo should not be altered. Paper should be A4 sized and not Letter sized.

```html
<!DOCTYPE html>
<html lang="en">
<head>
<meta charset="utf-8">
<title>Marlow Ridge Letterhead</title>
<link href="https://fonts.googleapis.com/css2?family=Didact+Gothic&display=swap" rel="stylesheet">
<style>
  :root {
    --backdrop: #e4e4e4;
    --paper: #ffffff;
    --brand-tile: #3a3936;
    --brand-gold: #d9a75a;
    --ink: #2b2b2b;
    --rule: #555555;
  }
  * { margin: 0; padding: 0; box-sizing: border-box; }
  html, body {
    width: 1200px;
    height: 968px;
    overflow: hidden;
    background: var(--backdrop);
    font-family: "Didact Gothic", "Century Gothic", sans-serif;
    color: var(--ink);
  }
  .letterhead {
    position: absolute;
    left: 289px;
    top: 44px;
    width: 622px;
    height: 880px;
    background: var(--paper);
    box-shadow: 0 6px 22px rgba(0,0,0,0.12);
  }
  .brand-tile {
    position: absolute;
    top: 0;
    right: 62px;
    width: 142px;
    height: 142px;
    background: var(--brand-tile);
    display: flex;
    flex-direction: column;
    align-items: center;
    justify-content: center;
    gap: 12px;
  }
  .brand-dot {
    width: 46px;
    height: 46px;
    border-radius: 50%;
    background: var(--brand-gold);
  }
  .brand-name {
    color: var(--brand-gold);
    font-size: 15px;
    letter-spacing: 0.5px;
  }
  .footer {
    position: absolute;
    left: 86px;
    width: 330px;
    top: 772px;
    text-align: center;
  }
  .footer-rule {
    height: 1px;
    background: var(--rule);
    margin-bottom: 12px;
  }
  .company-legal {
    font-size: 11px;
    letter-spacing: 0.6px;
    margin-bottom: 8px;
  }
  .address {
    font-size: 7.5px;
    margin-bottom: 6px;
  }
  .contacts {
    display: flex;
    justify-content: center;
    gap: 14px;
    font-size: 7.5px;
  }
  .contact {
    display: inline-flex;
    align-items: center;
    gap: 4px;
  }
  .contact svg { width: 8px; height: 8px; }
</style>
</head>
<body>
  <main class="letterhead">
    <div class="brand-tile">
      <div class="brand-dot"></div>
      <div class="brand-name">Marlow Ridge</div>
    </div>

    <footer class="footer">
      <div class="footer-rule"></div>
      <div class="company-legal">MARLOW RIDGE LLC</div>
      <div class="address">4810 Alder Crest Rd. Suite 12, Fairmont, OR 97215</div>
      <div class="contacts">
        <span class="contact">
          <svg viewBox="0 0 10 10"><circle cx="5" cy="5" r="4.5" fill="none" stroke="#2b2b2b"/><rect x="2.6" y="3.4" width="4.8" height="3.2" fill="none" stroke="#2b2b2b" stroke-width="0.8"/><path d="M2.6 3.4 L5 5.3 L7.4 3.4" fill="none" stroke="#2b2b2b" stroke-width="0.8"/></svg>
          info@marlowridge.com
        </span>
        <span class="contact">
          <svg viewBox="0 0 10 10"><circle cx="5" cy="5" r="4.5" fill="none" stroke="#2b2b2b"/><ellipse cx="5" cy="5" rx="1.8" ry="4.5" fill="none" stroke="#2b2b2b" stroke-width="0.7"/><path d="M0.5 5 H9.5" stroke="#2b2b2b" stroke-width="0.7"/></svg>
          www.marlowridge.com
        </span>
        <span class="contact">
          <svg viewBox="0 0 10 10"><circle cx="5" cy="5" r="4.5" fill="none" stroke="#2b2b2b"/><path d="M3.2 2.6 L4.3 3.7 L3.7 4.4 Q4.6 5.9 5.6 6.3 L6.3 5.7 L7.4 6.8 L6.6 7.6 Q4 7.2 2.4 3.4 Z" fill="#2b2b2b"/></svg>
          555-014-3333
        </span>
        <span class="contact">
          <svg viewBox="0 0 10 10"><circle cx="5" cy="5" r="4.5" fill="none" stroke="#2b2b2b"/><rect x="2.5" y="4" width="5" height="3" fill="#2b2b2b"/><rect x="3.5" y="2.4" width="3" height="1.6" fill="none" stroke="#2b2b2b" stroke-width="0.7"/></svg>
          555-014-2222
        </span>
      </div>
    </footer>
  </main>
</body>
</html>
```